Flyer/Poster design required for volunteer activities

We need a STRIKING A4 Poster/Flyer advertising our conservation volunteer program activities which are currently happening in the area. This poster is to advertise the program once people have arrived on the island or to locals. The program covers 5 months, May-September 2019 and is focused on conservation. I have attached the following:
- a flyer which was previously created (QMR Habitat Helpers 2019 sm)to advertise the program - would prefer it has a similar striking resemblance, but not essential
- A mock up document 'HHQMR On Island Poster_2019_v2' with text -Logos-Images

Target Market(s)

Everyone interested in Environmental Adventure/Hiking/Citizen Science

Industry/Entity Type

Tourism

Font styles to use
Sans Serif

Requirements
Must have
• -A travel conservation focus
• -Must use 'QMR-Background Image' as the background to the design
• -The info of where to get more information and the social media details must be prominent

```html
<!DOCTYPE html>
<html lang="en">
<head>
<meta charset="utf-8">
<title>Quill Marren Island – Conservation Volunteers 2019</title>
<link href="https://fonts.googleapis.com/css2?family=Montserrat:wght@400;500;600;700;800&family=Kaushan+Script&display=swap" rel="stylesheet">
<style>
  :root {
    --page: #e9e9e9;
    --sky-deep: #1766b3;
    --sky: #35a9e3;
    --sky-light: #7fd0f0;
    --sea: #1f86b8;
    --land: #3d6a35;
    --orange: #f0961a;
    --orange-deep: #e38410;
    --white: #ffffff;
    --ink-soft: rgba(255,255,255,0.92);
  }
  * { margin: 0; padding: 0; box-sizing: border-box; }
  html, body { width: 1200px; height: 1200px; overflow: hidden; }
  body {
    background: var(--page);
    font-family: "Montserrat", Arial, sans-serif;
    color: var(--white);
    position: relative;
  }
  .poster {
    position: absolute;
    left: 184px; top: 20px;
    width: 832px; height: 1160px;
    overflow: hidden;
    box-shadow: 0 6px 18px rgba(0,0,0,0.25);
  }
  .poster-backdrop {
    position: absolute; inset: 0;
    background:
      linear-gradient(180deg, var(--sky-deep) 0%, var(--sky) 30%, var(--sky-light) 52%, var(--sky) 62%, var(--sea) 74%, #2a8fa8 82%, var(--land) 92%, #2f5426 100%);
  }
  .info-panel {
    position: absolute; left: 56px; top: 440px; width: 720px; height: 640px;
    background: rgba(255,255,255,0.08);
  }
  .bird-photo {
    position: absolute; left: 0; top: 90px; width: 170px; height: 300px;
    background: radial-gradient(ellipse at 40% 50%, rgba(240,240,240,0.75), rgba(240,240,240,0) 70%);
  }
  .corner-mark {
    position: absolute; left: 77px; top: 78px; width: 75px; height: 75px;
    border-left: 14px solid var(--orange-deep);
    border-top: 14px solid var(--orange-deep);
  }
  .title-script {
    position: absolute; left: 558px; top: 40px;
    font-family: "Kaushan Script", cursive;
    font-size: 64px; color: var(--orange-deep);
    transform: rotate(-8deg);
  }
  .title-main {
    position: absolute; left: 112px; top: 112px;
    font-weight: 800; font-size: 80px; letter-spacing: 0;
    line-height: 1; white-space: nowrap;
  }
  .title-sub {
    position: absolute; left: 0; right: 0; top: 208px; text-align: center;
    padding-left: 70px;
    font-weight: 700; font-size: 35px; white-space: nowrap;
  }
  .date-band {
    position: absolute; left: 236px; top: 256px; width: 400px; height: 56px;
  }
  .date-band span {
    position: absolute; inset: 0; display: flex; align-items: center; justify-content: center;
    font-weight: 800; font-size: 23px; color: #fff3dc;
  }
  .tagline {
    position: absolute; left: 0; right: 0; text-align: center; padding-left: 70px; white-space: nowrap;
  }
  .tagline-main { top: 336px; font-size: 24px; font-weight: 500; }
  .tagline-sub { top: 368px; font-size: 19.5px; font-weight: 500; }
  .tagline-sub b { font-weight: 700; }
  .activity-photo {
    position: absolute; width: 106px; height: 106px; border-radius: 50%;
    border: 3px solid var(--orange);
  }
  .photo-bird { background: radial-gradient(circle at 55% 45%, #9a9a98, #5a6a3c 70%); }
  .photo-diver { background: radial-gradient(circle at 50% 40%, #2a3a48, #1a8fc4 65%); }
  .photo-forest { background: radial-gradient(circle at 50% 50%, #6b6a40, #3a5a28 70%); }
  .photo-insect { background: radial-gradient(circle at 50% 50%, #e8b8a8, #d89a88 70%); }
  .photo-hiker { background: linear-gradient(180deg, #8fc7e8 0%, #3d8fb8 55%, #7a7045 100%); }
  .activity {
    position: absolute; width: 222px;
  }
  .month-tag {
    display: inline-block; position: relative;
    font-weight: 800; font-size: 15px; padding: 0 14px 0 4px; line-height: 17px;
    background: linear-gradient(90deg, var(--orange-deep), var(--orange) 85%, rgba(240,150,26,0));
    color: #fff3dc;
  }
  .feature-week { margin-top: 4px; font-size: 16px; line-height: 15px; font-weight: 500; }
  .feature-week b { display: block; font-weight: 700; }
  .activity h3 { margin-top: 14px; font-size: 9px; font-weight: 700; text-transform: uppercase; }
  .activity ul { list-style: none; margin-top: 1px; }
  .activity li { font-size: 8.6px; line-height: 11.4px; padding-left: 3px; position: relative; }
  .activity li::before { content: "·"; position: absolute; left: 0; }
  .more-info {
    position: absolute; left: 160px; width: 440px; top: 958px; text-align: center;
    font-size: 15px; line-height: 20px; font-weight: 500;
  }
  .more-info b { font-weight: 700; }
  .follow {
    position: absolute; left: 160px; width: 440px; top: 1016px; text-align: center;
    font-size: 17px; font-weight: 700; letter-spacing: 0.5px;
  }
  .social {
    position: absolute; top: 1052px; display: flex; align-items: center; gap: 7px;
    font-size: 18px; font-weight: 500;
  }
  .social i {
    width: 16px; height: 16px; border-radius: 50%; background: var(--orange); display: block;
  }
  .social-facebook { left: 314px; }
  .social-instagram { left: 428px; }
  .program-mark {
    position: absolute; left: 652px; top: 1000px; width: 150px;
    display: flex; flex-direction: column; align-items: center; gap: 6px;
    font-size: 13px; font-weight: 700; text-align: center; line-height: 15px;
  }
  .program-mark i {
    width: 34px; height: 34px; border-radius: 50%; border: 2px solid var(--white); display: block;
  }
</style>
</head>
<body>
<main class="poster">
  <div class="poster-backdrop" role="img" aria-label="Photograph of blue sky with clouds over the island coastline, lagoon and green hills"></div>
  <div class="info-panel"></div>
  <div class="bird-photo" role="img" aria-label="Blurred photograph of a white seabird in flight"></div>

  <div class="corner-mark"></div>
  <div class="title-script">island</div>
  <h1 class="title-main">QUILL MARREN</h1>
  <h2 class="title-sub">CONSERVATION VOLUNTEERS</h2>

  <div class="date-band">
    <svg width="400" height="56" viewBox="0 0 400 56" aria-hidden="true">
      <path d="M18 14 C90 4 250 2 372 8 L396 12 L378 18 L392 26 L374 34 C300 50 140 54 28 46 L6 40 L24 32 L2 24 Z" fill="var(--orange)"/>
    </svg>
    <span>MAY - SEPTEMBER 2019</span>
  </div>

  <p class="tagline tagline-main">BE INVOLVED IN PROTECTING PARADISE</p>
  <p class="tagline tagline-sub">JOIN THE <b>QMR HABITAT HELPERS</b> PROGRAM 2019</p>

  <div class="activity-photo photo-bird" style="left:77px;top:430px" role="img" aria-label="Photograph of a seabird chick on the ground"></div>
  <div class="activity-photo photo-diver" style="left:316px;top:430px" role="img" aria-label="Photograph of a snorkeller recording data underwater"></div>
  <div class="activity-photo photo-forest" style="left:554px;top:430px" role="img" aria-label="Photograph of a volunteer walking through palm forest"></div>

  <section class="activity" style="left:79px;top:549px">
    <span class="month-tag">MAY 2019</span>
    <p class="feature-week">Feature Week:<b>19th - 26th May</b></p>
    <h3>Birds of Quill Marren Island</h3>
    <ul>
      <li>Ocean bird watching boat trips</li>
      <li>Guided tours of Woodhen and Currawong quarters</li>
      <li>Weekly lectures at the Quill Marren Island Museum</li>
      <li>Weekly screenings of documentaries on Bird and Island Conservation projects</li>
      <li>Self guided land bird survey tours</li>
    </ul>
  </section>

  <section class="activity" style="left:318px;top:549px">
    <span class="month-tag">JUNE 2019</span>
    <p class="feature-week">Feature Week:<b>3rd- 9th June</b></p>
    <h3>Quill Marren Island Marine Park</h3>
    <ul>
      <li>Marine pest monitoring with marine park staff</li>
      <li>Marine plastic &amp; debris clean up activities</li>
      <li>Screenings of marine conservation documentaries at the museum</li>
      <li>Weekly lectures on Marine Life at the Quill Marren Island Museum</li>
    </ul>
  </section>

  <section class="activity" style="left:557px;top:549px">
    <span class="month-tag">JULY 2019</span>
    <p class="feature-week">Feature Week:<b>21st - 28th July</b></p>
    <h3>Invasive Species</h3>
    <ul>
      <li>Guided walks to learn about the weed eradication program</li>
      <li>Weekly lectures on plants of Quill Marren Island</li>
      <li>Weekly screenings of documentaries on plant and island conservation projects</li>
      <li>Guided walks to Mount Talben</li>
      <li>Local tour guides include commentaries on island plants</li>
    </ul>
  </section>

  <div class="activity-photo photo-insect" style="left:95px;top:764px" role="img" aria-label="Photograph of a large stick insect held in hands"></div>
  <div class="activity-photo photo-hiker" style="left:417px;top:764px" role="img" aria-label="Photograph of a hiker looking over the lagoon"></div>

  <section class="activity" style="left:219px;top:762px">
    <span class="month-tag">AUGUST 2019</span>
    <p class="feature-week">Feature Week:<b>11th-19th August</b></p>
    <h3>Amazing Invertebrates</h3>
    <ul>
      <li>Guided night walks to learn about the island's invertebrates</li>
      <li>Weekly viewing and presentation of the Quill Marren Island Phasmid</li>
      <li>Weekly lectures on invertebrates of Quill Marren Island at the museum</li>
      <li>Weekly screenings of documentaries on island conservation projects</li>
    </ul>
  </section>

  <section class="activity" style="left:541px;top:762px">
    <span class="month-tag">SEPTEMBER 2019</span>
    <p class="feature-week">Feature Week:<b>1st-8th September</b></p>
    <h3>Protecting Paradise</h3>
    <ul>
      <li>Observational snorkel surveys with Marine Ecologists, to assess populations of Marren Anemonefish and other unique fish species</li>
      <li>Guided snorkel and glass bottom boat tour to assess coral health within the Quill Marren Island Marine Park</li>
      <li>Guided walks to learn about the island's conservation history</li>
    </ul>
  </section>

  <p class="more-info">See the QMR visitor centre for more information about<br>the <b>QMR Habitat Helpers</b> program for 2019</p>
  <p class="follow">FOLLOW US!</p>
  <div class="social social-facebook"><i></i><span>/hhqmr</span></div>
  <div class="social social-instagram"><i></i><span>@hhqmr</span></div>

  <div class="program-mark"><i></i><span>QMR Habitat Helpers</span></div>
</main>
</body>
</html>
```